" A empresa "desospitaliza" pacientes e monta toda estrutura necessária na residencia dele. (pacientes estaveis/pacientes terminais/pacientes com doenças cronicas /etc) "

```html
<!DOCTYPE html>
<html lang="pt-BR">
<head>
<meta charset="UTF-8">
<title>Instituto Vallora – Cartão de Visita</title>
<link rel="stylesheet" href="https://fonts.googleapis.com/css2?family=Questrial&family=Arimo:wght@400&display=swap">
<style>
  :root {
    --teal: #1b8a82;
    --orange: #ef8a3a;
    --ink: #3f3f3f;
    --frame: #b9b9b9;
    --paper: #ffffff;
    --divider: #8a8a8a;
  }
  * { margin: 0; padding: 0; box-sizing: border-box; }
  html, body {
    width: 1200px; height: 1200px; overflow: hidden;
    background: var(--paper);
  }
  .sheet {
    position: relative;
    width: 1200px; height: 1200px;
    background: var(--paper);
  }
  .sheet-frame {
    position: absolute;
    left: 5px; top: 19px; width: 1188px; height: 1158px;
    border: 2px solid var(--frame);
  }

  /* Front */
  .card-front {
    position: absolute;
    left: 135px; top: 218px; width: 1034px; height: 272px;
  }
  .front-band {
    position: absolute;
    left: 148px; top: 0; width: 886px; height: 272px;
    background: var(--teal);
    border-radius: 0 30px 30px 0;
  }
  .front-mark {
    position: absolute;
    left: 0; top: 47px; width: 178px; height: 178px;
    background: var(--orange);
    border-radius: 22px;
  }
  .front-mark-name {
    position: absolute;
    left: 200px; top: 112px;
    font-family: "Questrial", sans-serif;
    font-size: 38px; letter-spacing: 1px;
    color: var(--paper);
  }
  .front-title {
    position: absolute;
    right: 111px; top: 56px;
    text-align: right;
    font-family: "Questrial", sans-serif;
    color: var(--paper);
  }
  .front-title .name {
    font-size: 27px; font-variant: small-caps; letter-spacing: 1px; line-height: 30px;
  }
  .front-title .tagline { font-size: 23px; line-height: 28px; }
  .front-contact {
    position: absolute;
    right: 40px; top: 166px;
    text-align: right;
    font-family: "Arimo", sans-serif;
    font-style: normal;
    font-size: 23px; line-height: 27px;
    color: var(--paper);
  }

  /* Back */
  .card-back {
    position: absolute;
    left: 170px; top: 720px; width: 860px; height: 210px;
  }
  .back-brand {
    position: absolute;
    left: 0; top: 0; width: 330px;
    text-align: center;
  }
  .back-mark {
    display: block;
    width: 74px; height: 74px;
    margin: 2px auto 0;
    background: var(--teal);
    border-radius: 10px;
  }
  .back-name {
    margin-top: 42px;
    font-family: "Questrial", sans-serif;
    font-size: 31px; font-variant: small-caps; letter-spacing: 1.5px;
    color: var(--teal);
    line-height: 32px;
  }
  .back-tagline {
    font-family: "Questrial", sans-serif;
    font-size: 25px; color: var(--ink); line-height: 32px;
  }
  .back-divider {
    position: absolute;
    left: 381px; top: 24px; width: 2px; height: 166px;
    background: var(--divider);
  }
  .back-contact {
    position: absolute;
    left: 447px; top: 26px;
    font-family: "Arimo", sans-serif;
    font-style: normal;
    font-size: 21px; line-height: 25px;
    color: var(--ink);
  }
</style>
</head>
<body>
<main class="sheet">
  <div class="sheet-frame"></div>

  <section class="card-front">
    <div class="front-band"></div>
    <div class="front-mark"></div>
    <div class="front-mark-name">Vallora</div>
    <div class="front-title">
      <div class="name">Instituto Vallora</div>
      <div class="tagline">Atenção Domiciliar</div>
    </div>
    <address class="front-contact">
      <div>(00)0000-0000</div>
      <div>contato@vallora.com</div>
      <div>rua sem nome,00 bairro sem nome , cidade sem nome</div>
    </address>
  </section>

  <section class="card-back">
    <div class="back-brand">
      <span class="back-mark"></span>
      <div class="back-name">Instituto Vallora</div>
      <div class="back-tagline">Atenção Domiciliar</div>
    </div>
    <div class="back-divider"></div>
    <address class="back-contact">
      <div>Nome Sobrenome</div>
      <div>função</div>
      <div>(00)0000-0000</div>
      <div>contato@vallora.com</div>
      <div>rua sem nome, 00</div>
      <div>bairro sem nome , cidade sem nome</div>
    </address>
  </section>
</main>
</body>
</html>
```